Dential Clinic Business Card

We need a simple elegant business card. 2 sided. First side with our details, and 2nd side with appointment time rows.

Dark background preferred. Will consider monotone design, or colored. Surprise us.

Details:
SIDE1

Harwick Plaza Dental

Dr Milo Brent
BDSc(Tarn) MOPRVS

Shop 42, Harwick Plaza
8-22 Larch Avenue, Harwick VIC 3188
Phone: 03 9447 2835
email: info@harwickplazadental.com.au
site: www.harwickplazadental.com.au
_____________________________________
SIDE 2
Appointed Time ________________________
Notes _______________________

Target Market(s)

Dental Patients

Industry/Entity Type

Healthcare

Contact Information for Business Card

SIDE1

Harwick Plaza Dental

Dr Milo Brent
Shop 42, Harwick Plaza
Phone: 03 9447 2835
SIDE 2

Font styles to use
Other font styles liked:
• Comfortaa

Requirements
Must have
• Dr Milo Brent
BDSc(Tarn) MOPRVS

Address
Phone
Email
Website
Nice to have
• Simple elegant design with our logo.
Colored logo.
Light text on dark background - Side 1
Light background so can be written on with dark pen - SIde 2
Should not have
• Too many colors

```html
<!DOCTYPE html>
<html lang="en">
<head>
<meta charset="utf-8">
<title>Harwick Plaza Dental – Business Card</title>
<link rel="stylesheet" href="https://fonts.googleapis.com/css2?family=Montserrat:wght@300;400;500;700&display=swap">
<style>
  :root {
    --backdrop: #3b3c3e;
    --brand-blue: #1598d8;
    --brand-green: #7cb93a;
    --card-grey: #8a8b8d;
    --icon-dark: #2b2c2e;
    --ink: #1f1f1f;
    --paper: #ffffff;
  }
  * { margin: 0; padding: 0; box-sizing: border-box; }
  html, body {
    width: 1200px; height: 900px; overflow: hidden;
    background: var(--backdrop);
    font-family: "Montserrat", sans-serif;
  }
  .canvas { position: relative; width: 1200px; height: 900px; }
  .card {
    position: absolute; width: 600px; height: 343px;
    border-radius: 26px; overflow: hidden;
    box-shadow: 0 18px 40px rgba(0,0,0,.45);
  }
  .card svg { position: absolute; inset: 0; display: block; }
  .card--front { left: 60px; top: 70px; }
  .card--back { left: 540px; top: 485px; }

  .contact text { fill: var(--paper); font-family: "Montserrat", sans-serif; }
  .contact__name { font-size: 22px; font-weight: 300; letter-spacing: .5px; }
  .contact__name .bold { font-weight: 700; }
  .contact__credentials { font-size: 10.5px; font-weight: 400; letter-spacing: .8px; }
  .contact__line { font-size: 12px; font-weight: 400; letter-spacing: .2px; }

  .brand {
    position: absolute; display: flex; align-items: center; gap: 10px;
  }
  .brand__dot { width: 30px; height: 30px; border-radius: 50%; flex: none; }
  .brand__name {
    font-family: "Montserrat", sans-serif; font-weight: 300;
    font-size: 19px; letter-spacing: .5px; white-space: nowrap;
  }
  .card--front .brand { left: 30px; top: 180px; }
  .card--front .brand__dot { background: var(--brand-green); }
  .card--front .brand__name { color: var(--brand-green); }
  .card--back .brand { left: 160px; top: 34px; }
  .card--back .brand__dot { background: var(--paper); width: 34px; height: 34px; }
  .card--back .brand__name { color: var(--paper); font-size: 24px; }

  .appointment {
    position: absolute; left: 150px; top: 92px; width: 380px; height: 196px;
    background: var(--paper); padding: 30px 26px 0 38px;
    display: flex; flex-direction: column; gap: 16px;
  }
  .appointment__row {
    display: flex; align-items: flex-end; gap: 4px;
    font-size: 11px; font-weight: 500; color: var(--ink); letter-spacing: .4px;
  }
  .appointment__row:nth-child(2), .appointment__row:nth-child(4) { padding-left: 18px; }
  .appointment__fill { flex: 1; border-bottom: 1.5px dotted var(--ink); height: 1px; margin-bottom: 3px; }
</style>
</head>
<body>
<main class="canvas">

  <section class="card card--front" aria-label="Business card front">
    <svg viewBox="0 0 600 343" width="600" height="343">
      <rect class="front__bg" width="600" height="343" fill="var(--brand-blue)"/>
      <circle class="front__panel" cx="110" cy="172" r="215" fill="var(--paper)"/>
      <path class="front__arc" d="M271 30 A215 215 0 0 1 270.5 315" fill="none" stroke="var(--brand-green)" stroke-width="3"/>
      <circle cx="271" cy="30" r="5" fill="var(--brand-green)"/>
      <circle cx="270.5" cy="315" r="5" fill="var(--brand-green)"/>

      <g class="icons">
        <g transform="translate(295 62)">
          <circle r="17" fill="var(--icon-dark)" stroke="var(--brand-blue)" stroke-width="2.5"/>
          <circle cy="-4" r="4" fill="#fff"/>
          <path d="M-7 7 a7 6 0 0 1 14 0 z" fill="#fff"/>
        </g>
        <g transform="translate(316 112)">
          <circle r="17" fill="var(--icon-dark)" stroke="var(--brand-blue)" stroke-width="2.5"/>
          <path d="M-7 -6 l3 -2 3 4 -2 2 q2 4 5 5 l2 -2 4 3 -2 3 q-8 1 -13 -13z" fill="#fff"/>
        </g>
        <g transform="translate(325 167)">
          <circle r="17" fill="var(--icon-dark)" stroke="var(--brand-blue)" stroke-width="2.5"/>
          <rect x="-8" y="-6" width="16" height="12" rx="1" fill="#fff"/>
          <path d="M-8 -6 L0 1 L8 -6" fill="none" stroke="var(--icon-dark)" stroke-width="1.5"/>
        </g>
        <g transform="translate(319 222)">
          <circle r="17" fill="var(--icon-dark)" stroke="var(--brand-blue)" stroke-width="2.5"/>
          <path d="M0 9 C-3 4 -6 1 -6 -3 a6 6 0 0 1 12 0 C6 1 3 4 0 9z" fill="#fff"/>
          <circle cy="-3" r="2.2" fill="var(--icon-dark)"/>
        </g>
        <g transform="translate(295 282)">
          <circle r="17" fill="var(--icon-dark)" stroke="var(--brand-blue)" stroke-width="2.5"/>
          <g fill="none" stroke="#fff" stroke-width="1.4">
            <circle r="8"/><ellipse rx="3.5" ry="8"/><line x1="-8" x2="8"/>
            <line x1="-7" x2="7" y1="-4" y2="-4"/><line x1="-7" x2="7" y1="4" y2="4"/>
          </g>
        </g>
      </g>

      <g class="contact">
        <text class="contact__name" x="324" y="56">Dr <tspan class="bold">MILO</tspan> BRENT</text>
        <text class="contact__credentials" x="326" y="75">BDSc(Tarn) MOPRVS</text>
        <text class="contact__line" x="346" y="116">03 9447 2835</text>
        <text class="contact__line" x="354" y="171">info@harwickplazadental.com.au</text>
        <text class="contact__line" x="348" y="211">Shop 42, Harwick Plaza</text>
        <text class="contact__line" x="348" y="227">8-22 Larch Avenue,</text>
        <text class="contact__line" x="348" y="243">Harwick VIC 3188</text>
        <text class="contact__line" x="324" y="286">www.harwickplazadental.com.au</text>
      </g>
    </svg>
    <div class="brand">
      <span class="brand__dot"></span>
      <span class="brand__name">Harwick Plaza Dental</span>
    </div>
  </section>

  <section class="card card--back" aria-label="Business card back">
    <svg viewBox="0 0 600 343" width="600" height="343">
      <rect class="back__bg" width="600" height="343" fill="var(--card-grey)"/>
      <path class="back__wave" d="M0 343 H200 C240 343 245 290 260 265 C280 235 330 230 380 235 C430 240 440 260 480 255 C530 250 570 230 600 215 V343 Z" fill="var(--brand-blue)"/>
    </svg>
    <div class="brand">
      <span class="brand__dot"></span>
      <span class="brand__name">Harwick Plaza Dental</span>
    </div>
    <div class="appointment">
      <div class="appointment__row"><span>APPOINTED TIME</span><span class="appointment__fill"></span></div>
      <div class="appointment__row"><span>NOTES</span><span class="appointment__fill"></span></div>
      <div class="appointment__row"><span>APPOINTED TIME</span><span class="appointment__fill"></span></div>
      <div class="appointment__row"><span>NOTES</span><span class="appointment__fill"></span></div>
    </div>
  </section>

</main>
</body>
</html>
```